Byte Crew - Settle Inn

A flyer to promote a service by Byte Crew that provides IT set up in home when moving house.

It should be for print format (A4, A5 and an email friendly version)

Logos, previous flyer, image all attached.

Please use black, green and white as base colours.Please change boys sweater/jumper in the photo to green to match the logo.

Byte Crew are bring a helpdesk to your front door, saving you time and money. With a variety of packages to suit your needs, the Byte Crew aims to tackle both small and complex issues from setting up a home network to servicing the needs of a growing company.

Target Market(s)

Consumers moving house, Relocation agents, Real Estate agents

Requirements
Must have
• Logo, image, text all attached
• Use of green, black and white
Nice to have
• Also have coloured ties if you want them for design

```html
<!DOCTYPE html>
<html lang="en">
<head>
<meta charset="utf-8">
<title>Byte Crew – Settle Inn Flyer</title>
<link rel="stylesheet" href="https://fonts.googleapis.com/css2?family=Arimo:ital,wght@0,400;0,700;1,700&display=swap">
<style>
  :root {
    --green: #9be010;
    --green-deep: #5fa80a;
    --panel: #1d1e1e;
    --footer: #121212;
    --white: #ffffff;
    --ink: #0f1a0a;
  }
  * { margin: 0; padding: 0; box-sizing: border-box; }
  html, body { width: 848px; height: 1200px; overflow: hidden; background: var(--panel); }
  body { font-family: "Arimo", Arial, sans-serif; color: var(--white); }
  .flyer { position: relative; width: 848px; height: 1200px; overflow: hidden; background: var(--panel); }

  .hero-photo {
    position: absolute; left: 0; top: 0; width: 848px; height: 570px;
    background:
      radial-gradient(ellipse 260px 300px at 560px 250px, #d9b39a 0%, rgba(217,179,154,0) 70%),
      radial-gradient(ellipse 420px 180px at 500px 520px, #6fd12a 0%, rgba(111,209,42,0) 75%),
      linear-gradient(100deg, #3c5a4a 0%, #6f8f74 35%, #9aa89a 60%, #4d6b58 100%);
  }
  .headline {
    position: absolute; left: 20px; top: 22px;
    font-weight: 700; font-size: 62px; line-height: 66px; letter-spacing: 1px;
    color: var(--green);
    text-shadow: 2px 2px 0 var(--ink), -1px -1px 0 var(--ink), 1px -1px 0 var(--ink), -1px 1px 0 var(--ink), 3px 4px 6px rgba(0,0,0,.6);
  }
  .headline span { display: block; }
  .headline .indent { padding-left: 4px; }

  .intro { position: absolute; left: 0; top: 604px; width: 848px; text-align: center;
    font-size: 34px; font-weight: 700; }
  .brand-name { display: inline-flex; align-items: center; gap: 8px; margin: 0 28px; font-weight: 700; color: var(--white); }
  .brand-name .mark { width: 14px; height: 14px; background: var(--green); }

  .tagline { position: absolute; left: 52px; top: 680px; width: 720px;
    font-style: italic; font-weight: 700; font-size: 15.5px; line-height: 20px; }

  .package { position: absolute; left: 0; top: 740px; width: 848px; text-align: center; }
  .package h2 { display: inline-block; font-size: 19px; font-weight: 700; color: var(--green);
    border-bottom: 2px solid var(--green); padding-bottom: 1px; }

  .features { position: absolute; left: 30px; top: 788px; list-style: none;
    font-size: 16.5px; font-weight: 700; line-height: 22.4px; }
  .features li { position: relative; padding-left: 16px; }
  .features li::before { content: ""; position: absolute; left: 0; top: 8px; width: 3px; height: 10px; background: var(--green); border-top: 3px solid var(--panel); box-shadow: 0 -4px 0 -0.5px var(--green); }
  .features .wrap { display: block; padding-left: 0; }

  .footnotes { position: absolute; left: 30px; top: 1064px; font-style: italic; font-weight: 700;
    font-size: 12.5px; line-height: 16px; color: var(--green); }
  .footnotes p:first-child { padding-left: 8px; }

  .book-now { position: absolute; left: 541px; top: 1026px; width: 264px; height: 104px;
    border-radius: 8px; background: linear-gradient(180deg, #b6f03a 0%, var(--green) 55%, #7cc70c 100%);
    display: flex; align-items: center; padding-left: 16px;
    font-size: 32px; font-weight: 700; color: var(--white); text-decoration: none;
    box-shadow: 0 6px 10px rgba(0,0,0,.5); }

  .contact-bar { position: absolute; left: 0; top: 1164px; width: 848px; height: 36px;
    background: var(--footer); display: flex; align-items: center;
    font-size: 15px; font-weight: 700; color: var(--green); }
  .contact-bar .web { margin-left: 64px; }
  .contact-bar .email { margin-left: 86px; }
  .contact-bar .phone { margin-left: 86px; }
</style>
</head>
<body>
<main class="flyer">
  <div class="hero-photo" role="img" aria-label="Worried boy in large glasses and a green sweater holding two unplugged cables"></div>
  <h1 class="headline">
    <span>CAN’T REMEMBER</span>
    <span>WHAT TO</span>
    <span class="indent">PLUG IN</span>
    <span>WHERE?</span>
  </h1>

  <p class="intro">Do not fear, the <span class="brand-name"><span class="mark"></span>Byte Crew</span> is here!</p>

  <p class="tagline">We take all the pain out of moving house and get you set-up, online and connected before you can say the word Byte.</p>

  <div class="package"><h2>WELCOME HOME BYTE $425</h2></div>

  <ul class="features">
    <li>Pre-visit online assessment to ensure maximum use of our Crew’s time</li>
    <li>Ready:&nbsp; IT Health Check and Audit report</li>
    <li>Set:&nbsp; Connection of your wireless network for user access including passwords<span class="wrap">and parental control if desired</span></li>
    <li>Go: Set up of 3 computers and 1 printer</li>
    <li>Expanding the family: Connection of one additional device eg StreamBox, TabPad,<span class="wrap">PlayCube, Smart TV*</span></li>
    <li>Updating of software and virus security check</li>
    <li>Byte Crew Membership</li>
    <li>Includes travel cost and up to 4 hours of a Crew member’s time in your house</li>
    <li>1 month free on Byte@Home Packages**</li>
    <li>Awesome Byte Crew fridge magnet</li>
  </ul>

  <div class="footnotes">
    <p>*Each additional device set-up is charged at $35</p>
    <p>** Based on our annual packages and If signed within 14 days</p>
  </div>

  <a class="book-now" href="#">BOOK NOW</a>

  <footer class="contact-bar">
    <span class="web">www.bytecrew.example</span>
    <span class="email">Email booking@bytecrew.example</span>
    <span class="phone">Hotline 6100 2400</span>
  </footer>
</main>
</body>
</html>
```